Radiant Crossing - An Exciting Mission & Book Cover Project

Help me to inspire people to live their best life! This is a mission, not just a design project.
I need a Book Cover designed to keep me inspired on the process of writing my book.
Book Title: Radiant Crossing
Tag Line: Three Simple Steps to get out of your own way, SuperCharge your Life and Step into Purpose!
Author: Marlis Quenby

The three steps are: Ownership, Vision and Action (Not sure if this should be on the front or back of the book cover)

The book is a self-help, motivational book. Personal development.
The cover needs to be strong and capture peoples attention, especially with competing shelf space. I almost see a fire ball of flame or explosion that will grab peoples attention.
My company is The Lantern Institute. I have added the company logo and a few pages of my presentation and topic outline to give an idea.
Maybe: The Lantern Institute logo on back of the cover. website is marlisquenby.com

THOUGHT: People should be able to take a photo of them holding the book cover showing what area of life they want Radiant Crossing in. This is why the front cover must be so visual and powerful that they want to take a photo with it. Ie. Explosion, fire, strong and bold.

Target Market(s)

Anyone who feels stuck and needs to breakthrough and move forward in life.

Industry/Entity Type

Motivation

Font styles to use
Serif
Sans Serif

Colors
ec1f27
f37122
fbed22

Requirements
Must have
• The design must be STRONG, SIMPLE, STAND OUT ON BOOK SHELVES.
Must have an open file to swap the photo and copy out.

Back Cover Page
1) Summary
2) 2-3 testimonials. One sentence.
3) About the Author (maybe with photo)
4) Lantern Institute logo
5) Website: radiantcrossing.com and marlisquenby.com
Nice to have
• If my photo works somewhere that would be great. I will change the photo later.
Added Where's Your Harbor? a nice cover example.
Should not have
• Right now I am writing the summary for the back of the cover. For now use Loreum Ipsum text and 2-3 recommendations. Again, I will get these only later.

```html
<!DOCTYPE html>
<html lang="en">
<head>
<meta charset="utf-8">
<title>Radiant Crossing – Book Cover</title>
<link rel="stylesheet" href="https://fonts.googleapis.com/css2?family=Montserrat:wght@700;800&family=Open+Sans:wght@400;600;700&display=swap">
<style>
  :root {
    --ink: #111111;
    --paper: #ffffff;
    --frame: #7a716f;
    --red: #ec1f27;
    --orange: #f37122;
    --yellow: #fbed22;
    --muted: #2a2a2a;
  }
  * { margin: 0; padding: 0; box-sizing: border-box; }
  html, body { width: 1200px; height: 810px; overflow: hidden; background: var(--paper); }
  .cover { position: relative; width: 1200px; height: 810px; background: var(--paper); font-family: "Open Sans", sans-serif; overflow: hidden; }

  .frame-lines { position: absolute; inset: 0; }

  /* Back cover */
  .back-panel { position: absolute; left: 0; top: 0; width: 361px; height: 810px; background: #000; }
  .back-section { position: absolute; left: 42px; width: 300px; color: var(--paper); }
  .back-section h2 { font-weight: 400; font-size: 27px; line-height: 32px; text-decoration: underline; text-decoration-thickness: 1.5px; text-underline-offset: 4px; margin-bottom: 12px; }
  .back-section p { font-size: 11.4px; line-height: 19.8px; letter-spacing: 0.15px; }
  .summary { top: 101px; }
  .about { top: 517px; }

  /* Spine */
  .rotated { position: absolute; transform: rotate(-90deg); transform-origin: left top; white-space: nowrap; }
  .spine-title { left: 588px; top: 598px; font-family: "Open Sans", sans-serif; font-weight: 700; font-size: 25px; line-height: 26px; letter-spacing: 1.2px; color: var(--ink); }
  .spine-title .accent { color: var(--orange); }
  .institute-mark { position: absolute; left: 383px; top: 386px; width: 40px; height: 40px; border-radius: 50%; background: var(--orange); }
  .institute-name { left: 466px; top: 500px; color: var(--ink); font-family: "Open Sans", sans-serif; font-weight: 700; text-align: center; border-top: 1px solid var(--ink); border-bottom: 1px solid var(--ink); padding: 0 8px; }
  .institute-name .small { display: block; font-size: 10px; line-height: 12px; letter-spacing: 3px; }
  .institute-name .large { display: block; font-size: 15.5px; line-height: 18px; letter-spacing: 0.4px; }
  .spine-url { left: 506px; top: 577px; font-size: 12.6px; line-height: 14px; color: var(--ink); }

  /* Front cover */
  .fire { position: absolute; left: 700px; top: 0; width: 470px; height: 380px; }
  .author-photo { position: absolute; left: 627px; top: 176px; width: 400px; height: 634px;
    background: linear-gradient(180deg, rgba(90,90,90,0) 0%, #8a8a8a 22%, #5d5d5f 55%, #3f3f42 100%); }
  .title { position: absolute; left: 800px; top: 108px; width: 380px; text-align: center; font-family: "Montserrat", sans-serif; font-weight: 800; }
  .title .line-one { display: block; font-size: 46px; line-height: 46px; color: var(--ink); letter-spacing: 0.5px; }
  .title .line-two { display: block; font-size: 46px; line-height: 46px; color: var(--paper); margin-top: -2px; text-shadow: 2px 3px 3px rgba(0,0,0,0.55); }
  .subtitle { position: absolute; left: 872px; top: 215px; width: 232px; text-align: center; font-family: "Montserrat", sans-serif; font-weight: 700; font-size: 13.6px; letter-spacing: -0.2px; color: var(--ink); }
  .author-line { position: absolute; left: 653px; top: 769px; font-family: "Open Sans", sans-serif; font-size: 16px; letter-spacing: 1.2px; color: var(--paper); }

  .steps { position: absolute; left: 0; top: 0; }
  .step-label { font-family: "Open Sans", sans-serif; font-size: 15.5px; line-height: 32px; }
  .step-one { left: 977px; top: 781px; color: var(--paper); }
  .step-two { left: 1031px; top: 781px; color: var(--paper); }
  .step-three { left: 1084px; top: 781px; color: var(--ink); }
</style>
</head>
<body>
<div class="cover">

  <svg class="frame-lines" width="1200" height="810" viewBox="0 0 1200 810" aria-hidden="true">
    <g fill="none" stroke="var(--frame)" stroke-width="2.5">
      <polyline points="572,17 17,17 17,797 572,797"/>
      <polyline points="627,16 1183,16 1183,797 1080,797"/>
    </g>
  </svg>

  <!-- Back cover -->
  <div class="back-panel"></div>
  <section class="back-section summary">
    <h2>Summary</h2>
    <p>Lorem ipsum dolor sit amet, consectetur adipisc-ing elit. Pellentesque porttitor ex a mi ullamcorper maximus. Quisque consectetur sit amet enim ac semper. Sed metus nisi, ullamcorper quis magna nec, vestibulum vehicula augue. Praesent facilisis congue ullamcorper. Pellentesque vehicula varius dapibus. Sed faucibus felis ac ligula lobortis bibendum. Nulla vitae risus sit amet metus effici-tur auctor ac non ante. Mauris tincidunt pharetra dui et accumsan. Cras vel ullamcorper turpis, vitae placerat quam. Aliquam congue posuere urna, at maximus libero accumsan quis. Vivamus in vulputate elit. Nam pellentesque justo quis nunc egestas iaculis. Etiam metus orci, pulvinar eu leo eu, molestie elementum sapien. Proin ut mollis neque. Morbi sed metus lectus. Curabitur at mauris vestibulum tellus eleifend pellentesque.</p>
  </section>
  <section class="back-section about">
    <h2>About the Author</h2>
    <p>Lorem ipsum dolor sit amet, consectetur adipisc-ing elit. Pellentesque porttitor ex a mi ullamcorper maximus. Quisque consectetur sit amet enim ac semper. Sed metus nisi, ullamcorper quis magna nec, vestibulum vehicula augue. Praesent facilisis congue ullamcorper. Pellentesque vehicula varius dapibus. Sed faucibus felis ac ligula lobortis bibendum. Nulla vitae risus sit amet metus effici-tur auctor ac non ante. Mauris tincidunt pharetra dui et accumsan. Cras vel ullamcorper turpis,</p>
  </section>

  <!-- Spine -->
  <div class="institute-mark"></div>
  <div class="rotated institute-name"><span class="small">THE</span><span class="large">LANTERN INSTITUTE</span></div>
  <div class="rotated spine-url">radiantcrossing.com and marlisquenby.com</div>
  <div class="rotated spine-title">RADIANT&nbsp;&nbsp;<span class="accent">CROSSING</span></div>

  <!-- Front cover -->
  <svg class="fire" viewBox="0 0 470 380" role="img" aria-label="Burst of orange fire and flying dust behind the title">
    <defs>
      <radialGradient id="fireGlow" cx="55%" cy="38%" r="60%">
        <stop offset="0" stop-color="#f58a2a"/>
        <stop offset="0.45" stop-color="#f37122" stop-opacity="0.9"/>
        <stop offset="0.8" stop-color="#f59a5a" stop-opacity="0.35"/>
        <stop offset="1" stop-color="#ffffff" stop-opacity="0"/>
      </radialGradient>
    </defs>
    <ellipse cx="250" cy="150" rx="230" ry="200" fill="url(#fireGlow)"/>
  </svg>

  <div class="author-photo" role="img" aria-label="Black and white portrait of the author in a suit jacket, smiling"></div>

  <h1 class="title"><span class="line-one">RADIANT</span><span class="line-two">CROSSING</span></h1>
  <div class="subtitle">RAPID LIFE TRANSFORMATION</div>

  <svg class="steps" width="1200" height="810" viewBox="0 0 1200 810" aria-hidden="true">
    <polygon fill="var(--red)" points="993,329 1025,371 1009,371 1009,810 977,810 977,371 962,371"/>
    <polygon fill="var(--orange)" points="1046,467 1078,509 1062,509 1062,810 1031,810 1031,509 1015,509"/>
    <polygon fill="var(--yellow)" points="1100,533 1131,575 1115,575 1115,810 1084,810 1084,575 1068,575"/>
  </svg>
  <div class="rotated step-label step-one">Three Simple Steps to get out of your own way</div>
  <div class="rotated step-label step-two">SuperCharge your Life</div>
  <div class="rotated step-label step-three">Step into Purpose!</div>

  <div class="author-line">I’M MARLIS QUENBY</div>
</div>
</body>
</html>
```